Professional & Modern Website Design for Quarry Roost Fittings

Our company, a leader in custom furniture and joinery solutions for mining camps, needs a website overhaul. Our current site is looking dated and underwhelming, and we’re seeking a design that truly reflects our professionalism and expertise.

To Whom Are We Speaking?
Our target audience includes asset managers, procurement professionals, and senior-level management from international mining companies. We need a website that speaks directly to these key decision-makers, showcasing our value and expertise.

What We’re Looking For:
Fresh & Modern Aesthetic: We want our website to captivate visitors with a contemporary and sleek design.
Professional Appeal: The new design should convey our commitment to high-quality craftsmanship and service.
Visual Impact: Showcase our custom furniture and joinery work with stunning visuals that highlight our capabilities.
Brochure Alignment: The design should mirror the style and aesthetics of our attached brochure to ensure brand consistency and visual harmony.
Logo & Branding: We want to keep our current logo and branding. The red color should be retained but used sparingly as an accent color to complement the overall design.
Brand Book Usage: Attached is our Brand Book for our Hotel and Accommodation Company. Please use only the correct colors and text from this Brand Book for our Quarry Roost Fittings Brand to ensure consistency and coherence across our branding.
Structured Layout: We require a total of 8 pages, including:
Landing Page: Featuring a prominent contact button
About
Services: Interior Design, Manufacturing, Delivery & Installation
Products: Furniture Packages, Joinery, Upholstery, Beds & Bedding

Our Goals:
Elevate Our Brand: Create a site that mirrors our reputation and industry leadership.
Enhance User Experience: Ensure a seamless, engaging experience for visitors.
Showcase Our Work: Promote our projects and services with impact.

Must include:
Contact us button
Geographical Reach

Previous company website: www.quarryroostfittings.com.au (we wish to convert some of the content from this website to the new platform). Competitor websites that we like: www.dovetelle.com.au,

For functionality we would like it to be designed on Wix.

```html
<!DOCTYPE html>
<html lang="en">
<head>
<meta charset="utf-8">
<title>Quarry Roost Fittings — Website</title>
<link href="https://fonts.googleapis.com/css2?family=Montserrat:wght@300;400;500;600;700;800&display=swap" rel="stylesheet">
<style>
:root{
  --canvas:#e3e4e6;
  --white:#ffffff;
  --paper:#f4f4f5;
  --band:#efefef;
  --ink:#222222;
  --text:#444444;
  --muted:#888888;
  --red:#d7202b;
  --footer:#2a2829;
  --gold:#c29a55;
}
*{margin:0;padding:0;box-sizing:border-box}
html,body{width:1200px;height:5137px;overflow:hidden}
body{background:var(--canvas);font-family:'Montserrat',sans-serif;color:var(--ink);position:relative}
.abs{position:absolute}
.brand-block{left:0;width:1200px;top:1010px;text-align:center}
.brand-name{font-weight:800;font-size:68px;letter-spacing:4px;color:var(--ink);line-height:1}
.brand-sub{font-weight:500;font-size:30px;letter-spacing:2px;margin-top:14px;color:var(--ink)}
.site{left:94px;top:1240px;width:1016px;height:3810px;background:var(--white);overflow:hidden}
.hero{left:0;top:0;width:1016px;height:664px;background:linear-gradient(180deg,#6f6a64 0%,#8c857c 45%,#b8b2aa 75%,#9d978f 100%)}
.nav-brand{left:114px;top:22px;color:var(--white)}
.nav-brand .n1{font-weight:800;font-size:26px;letter-spacing:2px;line-height:1}
.nav-brand .n2{font-weight:500;font-size:11px;letter-spacing:1px;margin-top:4px}
.nav-links{left:548px;top:38px;display:flex;gap:18px;font-size:10px;font-weight:500;letter-spacing:1px;color:var(--white)}
.nav-cta{left:788px;top:26px;width:112px;height:36px;border:1.5px solid var(--white);color:var(--white);font-size:10px;font-weight:700;letter-spacing:1px;display:flex;align-items:center;justify-content:center}
.hero-arrows{left:885px;top:590px}
.services{left:0;top:664px;width:1016px;height:642px;background:linear-gradient(180deg,#f8f8f8,#ececec)}
.eyebrow{font-size:13px;font-weight:500;letter-spacing:1px;color:var(--ink);display:flex;align-items:center;gap:14px}
.eyebrow::after{content:"";width:50px;height:2px;background:var(--red)}
.headline{font-weight:300;font-size:32px;letter-spacing:1.5px;line-height:40px;color:var(--ink)}
.headline b{font-weight:800}
.label{font-size:10px;font-weight:700;letter-spacing:1px}
.card{height:230px;width:420px;background:var(--white);border:1px solid #e2e2e2;display:flex}
.card .ph{width:214px;height:100%}
.card .body{padding:62px 0 0 36px}
.card h3{font-weight:400;font-size:17px;letter-spacing:1px;line-height:22px}
.card h3 b{font-weight:800}
.link{font-size:9px;font-weight:600;letter-spacing:.5px;display:flex;align-items:center;gap:8px;margin-top:40px}
.tri{width:0;height:0;border-left:8px solid var(--red);border-top:5px solid transparent;border-bottom:5px solid transparent}
.intro{left:0;top:1306px;width:1016px;height:454px;background:var(--band)}
.intro p{font-size:11px;line-height:19px;color:var(--text);width:370px}
.project{top:2296px;width:288px;height:236px}
.proj-link{top:2556px}
.form-card{left:106px;top:2960px;width:380px;height:470px;background:var(--paper)}
.field-label{font-size:9px;font-weight:700;letter-spacing:.5px}
.field-label i{color:var(--red);font-style:normal}
.input{background:var(--white);height:32px;font-size:9px;color:var(--muted);padding:11px 14px}
.footer{left:0;top:3360px;width:1016px;height:450px;background:var(--footer);color:var(--white)}
.f-head{font-size:10px;font-weight:700;letter-spacing:.5px;line-height:15px}
.f-text{font-size:10px;color:#bbbbbb;line-height:15px}
.social{width:30px;height:30px;border:1px solid #555;border-radius:50%;display:flex;align-items:center;justify-content:center}
</style>
</head>
<body>

<div class="abs brand-block">
  <div class="brand-name">QUARRY ROOST</div>
  <div class="brand-sub">FITTINGS</div>
</div>

<main class="abs site">
  <section class="abs hero" role="img" aria-label="Photograph of a furnished lounge with sofa, armchairs, coffee table and timber wall panels"></section>
  <div class="abs nav-brand"><div class="n1">QUARRY ROOST</div><div class="n2">FITTINGS</div></div>
  <nav class="abs nav-links"><span>ABOUT</span><span>SERVICES</span><span>PRODUCTS</span></nav>
  <div class="abs nav-cta">CONTACT US</div>
  <svg class="abs hero-arrows" width="60" height="14" viewBox="0 0 60 14" fill="none" stroke="#fff" stroke-width="1.5"><path d="M24 7H2M8 1L2 7l6 6"/><path d="M34 7h22M50 1l6 6-6 6"/></svg>

  <section class="abs services"></section>
  <div class="abs eyebrow" style="left:368px;top:766px">QUARRY ROOST FITTINGS</div>
  <h1 class="abs headline" style="left:0;width:1016px;top:806px;text-align:center">INTERIOR DESIGN, <b>MANUFACTURING,</b><br><b>DELIVERY</b> &amp; INSTALLATION</h1>
  <div class="abs label" style="left:74px;top:946px">PRODUCTS</div>
  <svg class="abs" style="left:896px;top:944px" width="46" height="12" viewBox="0 0 46 12" fill="none" stroke-width="1.5"><path d="M18 6H2M7 1L2 6l5 5" stroke="#555"/><path d="M26 6h16M37 1l5 5-5 5" stroke="#bbb"/></svg>
  <div class="abs card" style="left:74px;top:978px">
    <div class="ph" role="img" aria-label="Photograph of a timber drawer with cutlery dividers" style="background:linear-gradient(135deg,#d7b893,#efe6dc)"></div>
    <div class="body"><h3>JOINERY<br><b>FURNITURE</b></h3><div class="link"><span class="tri"></span>VIEW PRODUCTS</div></div>
  </div>
  <div class="abs card" style="left:520px;top:978px">
    <div class="ph" role="img" aria-label="Photograph of upholstery fabric samples" style="background:linear-gradient(135deg,#3f6b5e,#8f9a8c 60%,#b6b0a6)"></div>
    <div class="body"><h3>UPHOLSTERY<br><b>FABRICS</b></h3><div class="link"><span class="tri"></span>VIEW PRODUCTS</div></div>
  </div>
  <div class="abs card" style="left:962px;top:978px">
    <div class="ph" role="img" aria-label="Photograph of an upholstered bed base" style="background:linear-gradient(135deg,#e4e2de,#b9b3ab)"></div>
  </div>

  <section class="abs intro"></section>
  <div class="abs eyebrow" style="left:112px;top:1422px">INTRODUCTION</div>
  <h2 class="abs headline" style="left:112px;top:1456px">WELCOME TO QUARRY<br>ROOST <b>FITTINGS</b></h2>
  <p class="abs" style="left:112px;top:1548px;font-size:11px;line-height:19px;color:var(--text);width:370px">Welcome to Quarry Roost Fittings, your trusted partner for custom furniture manufacturing. We specialize in delivering high-quality furniture solutions tailored to your specific needs while ensuring stringent quality control and efficient project management throughout the process.</p>
  <div class="abs" role="img" aria-label="Photograph of an upholstered dining chair with timber legs" style="left:576px;top:1358px;width:312px;height:466px;background:linear-gradient(180deg,#d9d3ca 0%,#c8c0b4 50%,#5a3e2c 62%,#4a3222 100%);border-radius:120px 120px 6px 6px"></div>

  <div class="abs" role="img" aria-label="Aerial photograph of an ochre and teal mining landscape" style="left:122px;top:1850px;width:444px;height:330px;background:linear-gradient(135deg,#b8543a,#d9a06a 40%,#4f8c86 70%,#c56a3f)"></div>
  <h2 class="abs headline" style="left:612px;top:1936px">QUARRY ROOST<br><b>FITTINGS</b></h2>
  <div class="abs" style="left:612px;top:2040px;font-size:16px;letter-spacing:.8px;line-height:22px;color:var(--text)">IS YOUR ULTIMATE FURNITURE<br>SOLUTIONS PARTNER.</div>

  <div class="abs label" style="left:72px;top:2260px">OUR PROJECTS</div>
  <svg class="abs" style="left:896px;top:2258px" width="46" height="12" viewBox="0 0 46 12" fill="none" stroke-width="1.5"><path d="M18 6H2M7 1L2 6l5 5" stroke="#555"/><path d="M26 6h16M37 1l5 5-5 5" stroke="#bbb"/></svg>
  <div class="abs project" role="img" aria-label="Photograph of a camp bedroom with double bed" style="left:74px;background:linear-gradient(180deg,#e9e8e6,#b7b4ae)"></div>
  <div class="abs project" role="img" aria-label="Photograph of a bed with timber bedside panel" style="left:376px;background:linear-gradient(180deg,#f2f1ef,#d6b894)"></div>
  <div class="abs project" role="img" aria-label="Photograph of a room with wardrobe and desk" style="left:678px;background:linear-gradient(180deg,#e6e4e0,#8b7157)"></div>
  <div class="abs project" role="img" aria-label="Photograph of timber furniture detail" style="left:980px;background:linear-gradient(180deg,#ececea,#c49a6a)"></div>
  <div class="abs link proj-link" style="left:74px;margin:0"><span class="tri"></span>VIEW PROJECT</div>
  <div class="abs link proj-link" style="left:376px;margin:0"><span class="tri"></span>VIEW PROJECT</div>
  <div class="abs link proj-link" style="left:678px;margin:0"><span class="tri"></span>VIEW PROJECT</div>
  <div class="abs link proj-link" style="left:980px;margin:0"><span class="tri"></span>VIEW PROJECT</div>

  <h2 class="abs headline" style="left:74px;top:2692px">GEOGRAPHICAL<br><b>REACH</b></h2>
  <div class="abs" style="left:74px;top:2776px;font-size:12px;letter-spacing:.5px;line-height:22px;color:var(--text);width:330px">WITH A GLOBAL PRESENCE, OUR SERVICES EXTEND TO AUSTRALIA, NEW ZEALAND, SOUTH EAST ASIA, AND THE UNITED ARAB EMIRATES.</div>
  <div class="abs" role="img" aria-label="World map highlighting Australia, New Zealand, South East Asia and the United Arab Emirates" style="left:456px;top:2660px;width:470px;height:230px;background:radial-gradient(ellipse at 70% 65%,rgba(194,154,85,.55),rgba(194,154,85,0) 40%),linear-gradient(180deg,#eeeeee,#e2e2e2);border-radius:8px"></div>

  <div class="abs" style="left:652px;top:3064px"><h2 class="headline">GET IN TOUCH<br><b>WITH US</b></h2>
    <div style="font-size:12px;letter-spacing:.5px;line-height:22px;color:var(--text);margin-top:18px;width:350px">LET'S GET THIS CONVERSATION STARTED. TELL US A BIT ABOUT YOURSELF, AND WE'LL GET IN TOUCH AS SOON AS WE CAN.</div></div>

  <section class="abs footer"></section>
  <div class="abs" style="left:72px;top:3570px"><div style="font-weight:800;font-size:34px;letter-spacing:2px;color:var(--white);line-height:1">QUARRY ROOST</div><div style="font-weight:500;font-size:16px;letter-spacing:1px;color:var(--white);margin-top:6px">FITTINGS</div></div>
  <div class="abs" style="left:456px;top:3520px">
    <div class="f-head">IF YOU HAVE ANY QUESTIONS,<br>LET US KNOW</div>
    <div class="f-text" style="margin-top:10px;padding-left:22px;position:relative"><svg style="position:absolute;left:0;top:2px" width="12" height="12" viewBox="0 0 24 24" fill="#d7202b"><path d="M6.6 10.8a15 15 0 006.6 6.6l2.2-2.2c.3-.3.7-.4 1-.2 1.1.4 2.3.6 3.6.6.6 0 1 .4 1 1V20c0 .6-.4 1-1 1A17 17 0 013 4c0-.6.4-1 1-1h3.5c.6 0 1 .4 1 1 0 1.3.2 2.5.6 3.6.1.3 0 .7-.2 1z"/></svg>Phone:<br>1300 555 014</div>
    <div class="f-head" style="margin-top:30px">FOLLOW US</div>
    <div style="display:flex;gap:10px;margin-top:12px"><span class="social"></span><span class="social"></span></div>
  </div>
  <div class="abs" style="left:708px;top:3520px">
    <div class="f-head">GET IN TOUCH<br>WITH US</div>
    <div class="f-text" style="margin-top:10px;padding-left:22px;position:relative"><svg style="position:absolute;left:0;top:2px" width="12" height="12" viewBox="0 0 24 24" fill="#d7202b"><path d="M6.6 10.8a15 15 0 006.6 6.6l2.2-2.2c.3-.3.7-.4 1-.2 1.1.4 2.3.6 3.6.6.6 0 1 .4 1 1V20c0 .6-.4 1-1 1A17 17 0 013 4c0-.6.4-1 1-1h3.5c.6 0 1 .4 1 1 0 1.3.2 2.5.6 3.6.1.3 0 .7-.2 1z"/></svg>Mobile:<br>+61 400 555 218</div>
    <div class="f-text" style="margin-top:16px;padding-left:22px;position:relative"><svg style="position:absolute;left:0;top:3px" width="12" height="10" viewBox="0 0 24 18" fill="#d7202b"><path d="M0 0h24v18H0z M2 2l10 8 10-8" stroke="#2a2829" stroke-width="2"/></svg>Email:<br>alex@quarryroostfittings.com.au<br>info@quarryroostfittings.com.au</div>
  </div>
  <div class="abs" style="left:72px;top:3762px;width:872px;height:1px;background:#444"></div>
  <svg class="abs" style="left:958px;top:3740px" width="36" height="36" viewBox="0 0 36 36"><circle cx="18" cy="18" r="18" fill="#d7202b"/><path d="M13 20l5-5 5 5" fill="none" stroke="#fff" stroke-width="1.8"/></svg>
  <div class="abs" style="left:0;width:1016px;top:3780px;text-align:center;font-size:9px;color:#bbb;letter-spacing:.3px">© COPYRIGHT 2024 QUARRY ROOST FITTINGS, ALL RIGHTS RESERVED</div>

  <form class="abs form-card">
    <div class="abs field-label" style="left:40px;top:30px">NAME<i>*</i></div>
    <div class="abs input" style="left:40px;top:46px;width:148px">Enter your name</div>
    <div class="abs field-label" style="left:196px;top:30px">PHONE<i>*</i></div>
    <div class="abs input" style="left:196px;top:46px;width:148px">Enter phone number</div>
    <div class="abs field-label" style="left:40px;top:96px">EMAIL<i>*</i></div>
    <div class="abs input" style="left:40px;top:112px;width:148px">Enter your email</div>
    <div class="abs field-label" style="left:196px;top:96px">ADDRESS<i>*</i></div>
    <div class="abs input" style="left:196px;top:112px;width:148px">Enter your address</div>
    <div class="abs field-label" style="left:40px;top:162px">MESSAGE<i>*</i></div>
    <div class="abs input" style="left:40px;top:178px;width:304px;height:62px">Enter your message</div>
    <div class="abs" style="left:40px;top:262px;width:304px;height:76px;background:var(--white);border:1px dashed #ccc;display:flex;align-items:center;justify-content:center;gap:10px;font-size:9px">
      <svg width="14" height="14" viewBox="0 0 24 24" fill="none" stroke="#333" stroke-width="2"><path d="M12 16V4M7 9l5-5 5 5M4 16v4h16v-4"/></svg>
      <span><u style="color:var(--red)">Choose file</u> or drop here</span></div>
    <div class="abs" style="left:40px;top:362px;display:flex;align-items:center;gap:8px;font-size:8px;color:var(--text)"><span style="width:13px;height:13px;border:1px solid #777;background:#fff"></span>I agree to the terms and conditions</div>
    <div class="abs" style="left:40px;top:402px;width:304px;height:36px;background:var(--red);color:var(--white);font-size:10px;font-weight:700;letter-spacing:1px;display:flex;align-items:center;justify-content:center">SEND MESSAGE
      <svg style="position:absolute;right:16px" width="14" height="14" viewBox="0 0 24 24" fill="#fff"><path d="M2 12L22 2 16 22l-4-8z"/></svg></div>
  </form>
</main>

</body>
</html>
```